Gift voucher for a photo shoot, folding card DIN long (21 x 9.8 cm)

Hello, I'm a professional photographer and need a new design for my gift voucher card for a photo shoot. The design should be applicable to all types of photo shoots (neutral). I prefer a sophisticated design. The folded card should be printed on both sides.
My data should be included: Logo, Address: Wendtaler Gasse 9, 07318 Gera, Email: fotograf@jonasbirkner.eu, Website: www.jonasbirkner.eu Tel.: 0176 / 4389025
Updates

Please design the folding card in DIN long format (105 x 210 mm, landscape format). The card should open horizontally. Please design the front with the words "Gift voucher for you" and my logo. Please make the logo small – the words "Gift voucher" should be in the foreground.
The colors - use elegant gray with gold or white font color.
The inside should contain the words: Photo shoot for ........ worth .....€, as well as my logo.
My contact details should be on the back.

Target Market(s)

Private customer

Colors

Designer to choose only greyscale colors for use in the design.

Requirements
Must have
• Noble appearance, a gift voucher that one likes to give away, words: Gift voucher for you, photo shoot for ..., worth .......€
Nice to have
• Noble appearance of the gift voucher, a gift voucher that you like to give away
Should not have
• no pictures

```html
<!DOCTYPE html>
<html lang="en">
<head>
<meta charset="utf-8">
<title>Gift Voucher – Jonas Birkner Fotograf</title>
<link href="https://fonts.googleapis.com/css2?family=Cinzel:wght@400;500&family=Poppins:wght@400;500;600&display=swap" rel="stylesheet">
<style>
  :root {
    --stage: #000000;
    --card: #989898;
    --gold: #f3ab5d;
    --gold-soft: rgba(243, 171, 93, 0.55);
    --gold-faint: rgba(243, 171, 93, 0.3);
    --white: #ffffff;
    --faint: rgba(255, 255, 255, 0.12);
  }
  html, body {
    margin: 0;
    padding: 0;
    width: 1200px;
    height: 704px;
    overflow: hidden;
    background: var(--stage);
  }
  .canvas {
    position: relative;
    width: 1200px;
    height: 704px;
    background: var(--stage);
  }
  .card {
    position: absolute;
    left: 145px;
    width: 910px;
    height: 219px;
    background: var(--card);
    overflow: hidden;
    font-family: "Cinzel", serif;
    color: var(--white);
  }
  .card--outside { top: 102px; }
  .card--inside { top: 383px; }

  /* brand block */
  .brand {
    position: absolute;
    text-align: center;
    transform: translateX(-50%);
    white-space: nowrap;
  }
  .brand__ring {
    display: block;
    margin: 0 auto;
    border: 2px solid var(--white);
    border-radius: 50%;
    box-sizing: border-box;
  }
  .brand__name {
    display: block;
    font-family: "Cinzel", serif;
    font-weight: 400;
    letter-spacing: 0.02em;
    line-height: 1;
  }
  .brand__role {
    display: block;
    font-family: "Poppins", sans-serif;
    font-weight: 500;
    letter-spacing: 0.35em;
    line-height: 1;
  }
  .brand--large { left: 111px; top: 26px; }
  .brand--large .brand__ring { width: 52px; height: 52px; margin-bottom: 10px; }
  .brand--large .brand__name { font-size: 22px; }
  .brand--large .brand__role { font-size: 9px; margin-top: 3px; }

  .brand--small { left: 824px; top: 138px; }
  .brand--small .brand__ring { width: 30px; height: 30px; margin-bottom: 5px; border-width: 1.5px; }
  .brand--small .brand__name { font-size: 14px; }
  .brand--small .brand__role { font-size: 5.5px; margin-top: 2px; }

  .brand--center { left: 355px; top: 113px; }
  .brand--center .brand__ring { width: 44px; height: 44px; margin-bottom: 7px; }
  .brand--center .brand__name { font-size: 21px; }
  .brand--center .brand__role { font-size: 7.5px; margin-top: 2px; }

  /* contact */
  .contact {
    position: absolute;
    left: 27px;
    top: 158px;
    display: grid;
    grid-template-columns: 160px auto;
    row-gap: 8px;
    font-family: "Poppins", sans-serif;
    font-size: 8.5px;
    color: var(--white);
  }
  .contact__item { display: flex; align-items: center; gap: 6px; line-height: 14px; }
  .contact__item b { font-weight: 600; }
  .contact__icon { width: 10px; height: 10px; flex: none; }

  /* illustration area */
  .illustration {
    position: absolute;
    left: 479px;
    top: 61px;
    width: 128px;
    height: 133px;
    border-radius: 12px;
    background: linear-gradient(160deg, var(--gold-soft), var(--gold-faint));
  }

  /* headlines */
  .headline {
    position: absolute;
    right: 28px;
    text-align: right;
    line-height: 1;
    white-space: nowrap;
    margin: 0;
    font-weight: 400;
  }
  .headline--gift { top: 40px; }
  .headline--gift .small { font-size: 30px; color: var(--white); }
  .headline--gift .large { font-size: 44px; color: var(--gold); }
  .headline--you { top: 84px; }
  .headline--you .small { font-size: 28px; color: var(--white); }
  .headline--you .large { font-size: 42px; color: var(--white); }

  .headline--shoot { top: 38px; font-size: 36px; color: var(--gold); }
  .headline--for { top: 74px; font-size: 28px; color: var(--white); }

  .recipient-line {
    position: absolute;
    left: 640px;
    top: 140px;
    width: 242px;
    height: 1px;
    background: var(--white);
  }
  .worth {
    position: absolute;
    left: 642px;
    top: 164px;
    width: 240px;
    display: flex;
    align-items: baseline;
    font-size: 25px;
    line-height: 1;
    white-space: nowrap;
  }
  .worth__dots {
    flex: 1;
    overflow: hidden;
    font-family: "Poppins", sans-serif;
    font-size: 18px;
    letter-spacing: 1px;
  }
  .serial {
    position: absolute;
    right: 28px;
    top: 203px;
    font-size: 7px;
    color: var(--white);
  }

  .watermark-ring {
    position: absolute;
    left: 4px;
    top: 3px;
    width: 214px;
    height: 214px;
    border: 6px solid var(--faint);
    border-radius: 50%;
    box-sizing: border-box;
  }

  .services {
    position: absolute;
    font-family: "Poppins", sans-serif;
    font-size: 14px;
    line-height: 19.5px;
    color: var(--white);
  }
  .services--left { left: 27px; top: 141px; }
  .services--right { left: 115px; top: 158px; }
  .services p { margin: 0; }
</style>
</head>
<body>
<div class="canvas">

  <section class="card card--outside">
    <div class="brand brand--large">
      <span class="brand__ring"></span>
      <span class="brand__name">Jonas Birkner</span>
      <span class="brand__role">FOTOGRAF</span>
    </div>

    <div class="contact">
      <div class="contact__item">
        <svg class="contact__icon" viewBox="0 0 10 10"><circle cx="5" cy="5" r="5" fill="var(--gold)"/><path d="M5 2.2a1.8 1.8 0 0 0-1.8 1.8c0 1.3 1.8 3.6 1.8 3.6s1.8-2.3 1.8-3.6A1.8 1.8 0 0 0 5 2.2z" fill="var(--white)"/></svg>
        <span>Wendtaler Gasse 9, 07318 Gera</span>
      </div>
      <div class="contact__item">
        <svg class="contact__icon" viewBox="0 0 10 10"><circle cx="5" cy="5" r="5" fill="var(--gold)"/><rect x="2.6" y="3.3" width="4.8" height="3.4" fill="none" stroke="var(--white)" stroke-width="0.8"/><path d="M2.6 3.4 5 5.2l2.4-1.8" fill="none" stroke="var(--white)" stroke-width="0.8"/></svg>
        <span><b>Email:</b> fotograf@jonasbirkner.eu</span>
      </div>
      <div class="contact__item">
        <svg class="contact__icon" viewBox="0 0 10 10"><circle cx="5" cy="5" r="5" fill="var(--gold)"/><path d="M3.2 2.6c.4-.3.8 0 1 .5l.3.8c.1.3-.1.5-.3.7.3.6.8 1.1 1.3 1.3.2-.2.4-.4.7-.3l.8.3c.5.2.8.6.5 1-.4.6-1 .8-1.6.5-1.3-.6-2.4-1.7-3-3-.3-.6-.1-1.2.3-1.8z" fill="var(--white)"/></svg>
        <span><b>Tel:</b> 0176 / 4389025</span>
      </div>
      <div class="contact__item">
        <svg class="contact__icon" viewBox="0 0 10 10"><circle cx="5" cy="5" r="5" fill="var(--gold)"/><circle cx="5" cy="5" r="2.6" fill="none" stroke="var(--white)" stroke-width="0.7"/><path d="M2.4 5h5.2M5 2.4c-1.2 1.4-1.2 3.8 0 5.2M5 2.4c1.2 1.4 1.2 3.8 0 5.2" fill="none" stroke="var(--white)" stroke-width="0.6"/></svg>
        <span><b>Website:</b> www.jonasbirkner.eu</span>
      </div>
    </div>

    <div class="illustration" role="img" aria-label="Gold line illustration of a camera with a flash burst"></div>

    <h1 class="headline headline--gift"><span class="small">GIFT </span><span class="large">VOUCHER</span></h1>
    <h2 class="headline headline--you"><span class="small">FOR </span><span class="large">YOU</span></h2>

    <div class="brand brand--small">
      <span class="brand__ring"></span>
      <span class="brand__name">Jonas Birkner</span>
      <span class="brand__role">FOTOGRAF</span>
    </div>
  </section>

  <section class="card card--inside">
    <div class="watermark-ring" aria-hidden="true"></div>

    <div class="services services--left">
      <p>Family</p>
      <p>Wedding</p>
      <p>Portrait</p>
    </div>
    <div class="services services--right">
      <p>Business</p>
      <p>Career</p>
    </div>

    <div class="brand brand--center">
      <span class="brand__ring"></span>
      <span class="brand__name">Jonas Birkner</span>
      <span class="brand__role">FOTOGRAF</span>
    </div>

    <div class="illustration" role="img" aria-label="Gold line illustration of a camera with a flash burst"></div>

    <h1 class="headline headline--shoot">PHOTO SHOOT</h1>
    <h2 class="headline headline--for">FOR</h2>
    <div class="recipient-line"></div>
    <div class="worth"><span>WORTH</span><span class="worth__dots">..............................................</span><span>€</span></div>
    <div class="serial">NR:</div>
  </section>

</div>
</body>
</html>
```